New Organic Skin Care Line Needs to Design a Product Label

***THE WINNER OF THIS PROJECT WILL MOST LIKELY BECOME THE EXCLUSIVE DESIGNER FOR OUR OTHER PRODUCT LABELS***

We need a label design for a new organic skin care product line called "Maple Fern Gala." This specific product is a 100% pure organic coconut oil. It's used for skin hydration, protection, and makeup removal.

Info to include on front label:

1. Logo: Maple Fern Gala (attached)
2. Product Name: Pure Coconut Oil (emphasize "organic" somewhere)
3. Slogan: Hydrate your skin and hair.
4. Size: 8 FL OZ 236mL

Attached is:

1. The brand logo "Maple Fern Gala" with a white background.
2. An image of the bottle we will use.
3. An image of the bottle with lines to show the size and placement of the label.
4. The brand logo "Maple Fern Gala" with a black background. (photoshop file)

What we need:

A simple mock up of the front side of the label on the bottle. We first want to know what it will look like on the bottle given the size and dimensions.

- We would like one label with a white background (including the logo with a white background).
- We would like a second label with a black background (including the logo with a black background, just need to make the black font white instead of black).

We can get a great idea of what to expect from the front side of the label so we will complete the back side once we identify a winner.
Updates

Apologies, but we are now using a different bottle. The previous one is now discontinued. Please view the two most recent images uploaded. One is an image of the new bottle by itself. The other is an image of that bottle with instructions. Please use your most recent designs on the new bottle. Feel free to make any modifications you see fit to compliment the new bottle shape. Added Friday, March 18, 2016

Reason: We are still working with the label company to finalize the size. Once the size is confirmed we will have to tweak labels based on finalized measurements.

Target Market(s)

Women, 18-70

Industry/Entity Type

Skin Care Product

Font styles to use
Decorative
Script

Requirements
Must have
• -"shabby sheek" and "cute" theme
• -soft organic feel
• -the ingredients are organic, pure, and natural. That should be an essence of the label.

```html
<!DOCTYPE html>
<html lang="en">
<head>
<meta charset="utf-8">
<title>Maple Fern Gala – Pure Coconut Oil Label</title>
<link href="https://fonts.googleapis.com/css2?family=Cinzel:wght@400;600&family=Cormorant+Garamond:wght@600&family=Josefin+Sans:wght@300&display=swap" rel="stylesheet">
<style>
  :root {
    --backdrop: #f9efd9;
    --label-cream: #fdfcef;
    --ink-brown: #2f2720;
    --berry: #e0185f;
    --berry-deep: #c40f4f;
    --leaf-green: #2f9a3a;
    --rule-grey: #8a8580;
    --coconut-brown: #a55a22;
    --coconut-white: #f4f0e2;
    --splash-grey: #d9d5cb;
  }
  html, body {
    margin: 0;
    padding: 0;
    width: 1200px;
    height: 1200px;
    overflow: hidden;
    background: var(--backdrop);
  }
  .canvas {
    position: relative;
    width: 1200px;
    height: 1200px;
  }
  .label {
    position: absolute;
    left: 100px;
    top: 100px;
    width: 1000px;
    height: 1000px;
    border-radius: 50%;
    background: var(--label-cream);
    overflow: hidden;
    text-align: center;
    box-shadow: 0 6px 30px rgba(120, 95, 60, 0.12);
  }
  .brand-name {
    position: absolute;
    top: 296px;
    left: 0;
    width: 100%;
    margin: 0;
    font-family: "Cinzel", serif;
    font-weight: 400;
    font-size: 29px;
    letter-spacing: 0.32em;
    color: var(--ink-brown);
  }
  .product-name {
    position: absolute;
    top: 370px;
    left: 0;
    width: 100%;
    margin: 0;
    font-family: "Cormorant Garamond", serif;
    font-weight: 600;
    font-size: 104px;
    line-height: 1;
    letter-spacing: 0.005em;
    color: var(--ink-brown);
  }
  .slogan-band {
    position: absolute;
    top: 483px;
    left: 139px;
    width: 696px;
    height: 41px;
    background: linear-gradient(90deg, var(--berry-deep), var(--berry) 50%, var(--berry-deep));
    display: flex;
    align-items: center;
    justify-content: center;
  }
  .slogan {
    margin: 0;
    font-family: "Cinzel", serif;
    font-weight: 600;
    font-size: 27px;
    letter-spacing: 0.02em;
    color: #fff4ec;
  }
  .organic-claim {
    position: absolute;
    top: 540px;
    left: 0;
    width: 100%;
    margin: 0;
    padding-right: 40px;
    box-sizing: border-box;
    font-family: "Josefin Sans", sans-serif;
    font-weight: 300;
    font-size: 36px;
    color: var(--leaf-green);
  }
  .hero-art {
    position: absolute;
    top: 590px;
    left: 0;
    width: 1000px;
    height: 300px;
    background:
      radial-gradient(ellipse 170px 110px at 540px 150px, var(--coconut-brown) 0%, rgba(165, 90, 34, 0.55) 55%, rgba(165, 90, 34, 0) 100%),
      radial-gradient(ellipse 120px 80px at 420px 190px, var(--coconut-white) 0%, rgba(244, 240, 226, 0) 100%),
      radial-gradient(ellipse 220px 60px at 480px 260px, rgba(47, 154, 58, 0.55) 0%, rgba(47, 154, 58, 0) 100%),
      linear-gradient(180deg, rgba(217, 213, 203, 0) 30%, var(--splash-grey) 80%, #cfcac0 100%);
  }
  .size-block {
    position: absolute;
    top: 905px;
    left: 0;
    width: 100%;
    display: flex;
    justify-content: center;
  }
  .size {
    margin: 0;
    padding: 8px 14px 10px;
    border-top: 1.5px solid var(--rule-grey);
    border-bottom: 1.5px solid var(--rule-grey);
    font-family: "Cormorant Garamond", serif;
    font-weight: 600;
    font-size: 27px;
    letter-spacing: 0.04em;
    color: var(--ink-brown);
    background: rgba(253, 252, 239, 0.6);
  }
</style>
</head>
<body>
  <main class="canvas">
    <section class="label">
      <p class="brand-name">MAPLE FERN GALA</p>
      <h1 class="product-name">Pure Coconut Oil</h1>
      <div class="slogan-band">
        <p class="slogan">HYDRATE YOUR SKIN AND HAIR</p>
      </div>
      <p class="organic-claim">100% ORGANIC</p>
      <div class="hero-art" role="img" aria-label="Split coconut halves and a whole coconut resting on green leaves over a splash of clear water"></div>
      <div class="size-block">
        <p class="size">8 FL OZ 236ML</p>
      </div>
    </section>
  </main>
</body>
</html>
```